Business Card Design Z9 MOTORS

Hi firstly I would like you to design a professional logo for my company. By using words " Z9 Auto Spares & Haulage".
We are an auto dismantling company where we buy wrecks/cars for dismantling and selling salvageable parts again.

Hi every one,

Thank you for posting the designs. But unfortunately non of these designs have the logo that I would prefer for my company. I will be branding the logo quite extensively, therefore please design some professional looking ones.

Thanks

Industry/Entity Type

Business

Contact Information for Business Card

Z9 Auto Spares & Haulage, 472 Kowhai Bend Rd, Fernmoor, Wellington
T: 04 7261048, F: 04 7261049, E: dean.morrow@z9motors.example.nz, W: www.z9motors.example.nz
Name: Dean L Morrow
Managing Director
Mob: 027418906

At the bottom of card " WE PAY TOP $$$$ FOR ANY UNWANTED VEHICLES FOR FOR DISMANTLING CALL US NOW 0800372815"

```html
<!DOCTYPE html>
<html lang="en">
<head>
<meta charset="utf-8">
<title>Z9 Motors Business Card</title>
<link href="https://fonts.googleapis.com/css2?family=Michroma&display=swap" rel="stylesheet">
<style>
  :root {
    --stage: #e6e8eb;
    --card-white: #ffffff;
    --brand-blue: #1fb0ec;
    --ink: #3a3a3a;
    --ink-soft: #5a5a5a;
    --ribbon-light: #e4e4e4;
    --ribbon-dark: #a9a9a9;
    --ribbon-fold: #7d7d7d;
  }
  * { box-sizing: border-box; margin: 0; padding: 0; }
  html, body {
    width: 1200px; height: 898px; overflow: hidden;
    background: var(--stage);
    font-family: "Michroma", "Arial", sans-serif;
  }
  .canvas { position: relative; width: 1200px; height: 898px; }
  .card {
    position: absolute; top: 300px;
    width: 530px; height: 303px;
    background: var(--card-white);
    box-shadow: 0 10px 26px rgba(0,0,0,0.18);
    overflow: hidden;
  }
  /* Back side */
  .card--back { left: 48px; }
  .card--back .band {
    position: absolute; top: 0; bottom: 0; width: 130px;
    background: var(--brand-blue);
  }
  .card--back .band--left { left: 0; }
  .card--back .band--right { right: 0; }
  .brand-name {
    color: var(--brand-blue);
    font-size: 15px;
    line-height: 1.35;
    letter-spacing: 0.5px;
    display: flex; align-items: center; gap: 8px;
  }
  .brand-name .brand-dot {
    width: 12px; height: 12px; border-radius: 50%;
    background: var(--brand-blue); flex: none;
  }
  .card--back .brand-name {
    position: absolute; left: 130px; right: 130px; top: 0; bottom: 0;
    justify-content: center; padding: 0 16px;
  }
  .slogan {
    position: absolute; left: 140px; right: 140px; bottom: 14px;
    color: var(--ink-soft); font-size: 5.6px; line-height: 1.6;
    text-align: center; letter-spacing: 0.2px; text-transform: uppercase;
  }
  .slogan .call { color: var(--brand-blue); }
  /* Front side */
  .card--front { left: 622px; }
  .card--front .panel-blue {
    position: absolute; top: 0; right: 0; bottom: 0; width: 178px;
    background: var(--brand-blue);
  }
  .name-ribbon {
    position: absolute; top: 64px; right: 12px; width: 300px; height: 28px;
    background: linear-gradient(180deg, var(--ribbon-light), var(--ribbon-dark));
    display: flex; align-items: center; justify-content: center;
    color: var(--ink); font-size: 7.2px; letter-spacing: 0.3px;
    text-transform: uppercase; white-space: nowrap; padding: 0 10px;
  }
  .name-ribbon::before {
    content: ""; position: absolute; left: 0; bottom: -10px;
    border-top: 10px solid var(--ribbon-fold);
    border-left: 12px solid transparent;
  }
  .name-ribbon .divider { margin: 0 6px; }
  .card--front .brand-name {
    position: absolute; left: 58px; top: 104px; width: 230px;
  }
  .contact {
    position: absolute; left: 26px; bottom: 18px;
    color: var(--ink-soft); font-size: 7.5px; line-height: 1.55;
  }
  .contact .address { margin-bottom: 7px; }
  .contact-line { display: flex; align-items: center; gap: 6px; }
  .contact-line svg { width: 9px; height: 9px; fill: var(--ink); flex: none; }
</style>
</head>
<body>
<main class="canvas">

  <section class="card card--back" aria-label="Card back">
    <div class="band band--left"></div>
    <div class="band band--right"></div>
    <div class="brand-name"><span class="brand-dot"></span><span>Z9 Auto Spares<br>&amp; Haulage</span></div>
    <p class="slogan">We pay top $$$$ for any unwanted vehicles for dismantling<br><span class="call">Call us now 0800372815</span></p>
  </section>

  <section class="card card--front" aria-label="Card front">
    <div class="panel-blue"></div>
    <div class="name-ribbon">Dean L Morrow<span class="divider">|</span>Managing Director</div>
    <div class="brand-name"><span class="brand-dot"></span><span>Z9 Auto Spares<br>&amp; Haulage</span></div>

    <div class="contact">
      <p class="address">472 Kowhai Bend Rd<br>Fernmoor, Wellington</p>
      <p class="contact-line">
        <svg viewBox="0 0 10 10"><path d="M2 0.5 L3.6 2.6 L2.8 3.6 Q4 6 6.4 7.2 L7.4 6.4 L9.5 8 L8.4 9.5 Q1 8 0.5 1.6 Z"/></svg>
        T: 04 7261048
      </p>
      <p class="contact-line">
        <svg viewBox="0 0 10 10"><path d="M2.5 0.5 H7.5 V3 H2.5 Z M0.5 3.5 H9.5 V7.5 H8 V6 H2 V7.5 H0.5 Z M2.8 6.6 H7.2 V9.5 H2.8 Z"/></svg>
        F: 04 7261049
      </p>
      <p class="contact-line">
        <svg viewBox="0 0 10 10"><path d="M3 0 H7 A1 1 0 0 1 8 1 V9 A1 1 0 0 1 7 10 H3 A1 1 0 0 1 2 9 V1 A1 1 0 0 1 3 0 Z M3 1.5 V7.5 H7 V1.5 Z" fill-rule="evenodd"/></svg>
        M: 027418906
      </p>
      <p class="contact-line">
        <svg viewBox="0 0 10 10"><path d="M0 2 H10 V8 H0 Z M0.8 2.6 L5 5.6 L9.2 2.6 V3.4 L5 6.4 L0.8 3.4 Z" fill-rule="evenodd"/></svg>
        dean.morrow@z9motors.example.nz
      </p>
      <p class="contact-line">
        <svg viewBox="0 0 10 10"><path d="M5 0 A5 5 0 1 1 4.99 0 Z M5 1.2 A3.8 3.8 0 1 0 5.01 1.2 Z M4.4 1.2 H5.6 V8.8 H4.4 Z M1.2 4.4 H8.8 V5.6 H1.2 Z" fill-rule="evenodd"/></svg>
        www.z9motors.example.nz
      </p>
    </div>
  </section>

</main>
</body>
</html>
```